Very Simple/Minimal Business Card Design Project

The company operates in the industrial maritime infrastructure sector in Brazil. You can find more information on our website www.navelquor.com.br WE NEED TO LOOK POWERFUL AND SERIOUS
I have attached a copy of the old cards. We would like something more professional / industrial / sexy that also includes the position.

The card can be double sided or not. We would like you to propose as many options.

Thank you
Updates

Many thanks, do let me know if you have any questions. I am under a lot of time pressure to try and have them printed over the next days or so.

Please could you use the following information

for the address: Rua Tapiraçu, 418 - Centro, Rio de Janeiro, 20135-070, Brasil

for the mobile: +55 21 8372 9041
for the landline: +55 21 4067 3859

and position:  Diretor Geral

Thakn you

Target Market(s)

Shipowners, bankers, industrial companies

Industry/Entity Type

Industrial

Requirements
Must have
• POWERFUL
SERIOUS
SOLID
BIG CORPORATION

```html
<!DOCTYPE html>
<html lang="pt-BR">
<head>
<meta charset="utf-8">
<title>Navelquor – Business Card</title>
<link rel="stylesheet" href="https://fonts.googleapis.com/css2?family=Roboto:wght@400;500;700&display=swap">
<style>
  :root {
    --backdrop: #e9e6e1;
    --card: #ffffff;
    --navy: #1f2f7a;
    --green: #1a9a3c;
    --grey: #6b6b6b;
    --rule: #d6d6d6;
  }
  html, body {
    margin: 0;
    padding: 0;
    width: 1200px;
    height: 901px;
    overflow: hidden;
    background: var(--backdrop);
    font-family: "Roboto", Arial, sans-serif;
  }
  .card {
    position: absolute;
    left: 300px;
    top: 276px;
    width: 600px;
    height: 348px;
    background: var(--card);
    box-shadow: 0 6px 18px rgba(0,0,0,0.18);
    overflow: hidden;
  }
  .card__bands {
    position: absolute;
    inset: 0;
  }
  .brand {
    position: absolute;
    left: 51px;
    top: 77px;
    display: flex;
    align-items: center;
    gap: 14px;
  }
  .brand__mark {
    width: 68px;
    height: 68px;
    background: var(--green);
  }
  .brand__name {
    font-weight: 700;
    font-size: 45px;
    letter-spacing: 0.5px;
    color: var(--navy);
  }
  .person {
    position: absolute;
    left: 53px;
    top: 193px;
    width: 507px;
  }
  .person__name {
    font-size: 22px;
    font-weight: 500;
    color: var(--navy);
    margin: 0;
    line-height: 26px;
  }
  .person__role {
    font-size: 12.5px;
    line-height: 16px;
    color: var(--grey);
    margin: 4px 0 0;
    letter-spacing: 0.3px;
  }
  .person__rule {
    height: 1px;
    background: var(--rule);
    margin: 3px 0 7px;
  }
  .person__email {
    font-size: 13px;
    line-height: 16px;
    color: var(--grey);
    margin: 0;
  }
  .contact {
    position: absolute;
    right: 45px;
    text-align: right;
    font-size: 13px;
    font-style: normal;
    color: var(--grey);
    line-height: 21px;
    margin: 0;
  }
  .contact--address { top: 156px; }
  .contact--phones { top: 248px; line-height: 22px; }
</style>
</head>
<body>
  <div class="card">
    <svg class="card__bands" width="600" height="348" viewBox="0 0 600 348" aria-hidden="true">
      <polygon points="0,0 600,0 600,10 0,4" fill="var(--green)"/>
      <polygon points="0,343 600,330 600,348 0,348" fill="var(--navy)"/>
    </svg>

    <div class="brand">
      <div class="brand__mark"></div>
      <div class="brand__name">NAVELQUOR</div>
    </div>

    <address class="contact contact--address">
      Rua Tapiraçu 418<br>
      Centro<br>
      CEP 20135-070<br>
      Rio de Janeiro
    </address>

    <div class="person">
      <p class="person__name">Rafael Montenegro</p>
      <p class="person__role">DIRETOR GERAL</p>
      <div class="person__rule"></div>
      <p class="person__email">rafael@navelquor.com.br</p>
    </div>

    <p class="contact contact--phones">
      T: +55 21 4067 3859<br>
      M: +55 21 8372 9041
    </p>
  </div>
</body>
</html>
```